Graphic Design Project

I am looking for a designer to create three simple kitchen tea towel designs using the following text (insert images where appropriate):

'Everything I am, I owe to spaghetti' - Marta Velucci (prefer red)

'Coogee, Bronte, Clovelly, Tamarama, Bondi' (These are names of Sydney beaches. Bondi is the most famous.)

'Desperate Housewife'

Artwork parameters for tea towels: 43cm width X 75cm length. The target market is 25 - 40yr old women.

The text should take up most of the available space on the towel.

There is the opportunity for ongoing work for the right designer.

Thank you for your time.

Target Market(s)

Women aged 25 - 40 who live in Sydney.

Industry/Entity Type

Graphic Design

Requirements
Nice to have
• The feel of the following website:
http://www.plumforkglow.com/

```html
<!DOCTYPE html>
<html lang="en">
<head>
<meta charset="utf-8">
<title>Tea Towel Collection</title>
<link rel="stylesheet" href="https://fonts.googleapis.com/css2?family=Short+Stack&family=Pinyon+Script&family=Titan+One&family=Lilita+One&family=Gochi+Hand&family=Tinos&family=Sniglet&display=swap">
<style>
  :root {
    --sky: #00aeef;
    --sky-light: #5bc8f5;
    --sky-deep: #1b75bb;
    --teal: #00a99d;
    --wine: #9b1c2e;
    --red: #ed1c24;
    --plum: #92278f;
    --plum-text: #f6e6f4;
    --sun: #fbb040;
    --tangerine: #f7941d;
    --coral: #f15a29;
    --white: #ffffff;
    --petal-orange: #f26522;
    --petal-pink: #c0359a;
    --noodle: #f2e33a;
  }
  html, body {
    margin: 0;
    padding: 0;
    width: 1200px;
    height: 693px;
    overflow: hidden;
    background: var(--white);
  }
  .towel-set { display: block; width: 1200px; height: 693px; }

  .fill-sky { fill: var(--sky); }
  .fill-sky-light { fill: var(--sky-light); }
  .fill-sky-deep { fill: var(--sky-deep); }
  .fill-teal { fill: var(--teal); }
  .fill-wine { fill: var(--wine); }
  .fill-red { fill: var(--red); }
  .fill-white { fill: var(--white); }
  .fill-sun { fill: var(--sun); }
  .fill-tangerine { fill: var(--tangerine); }

  .badge { fill: var(--white); }
  .banner { fill: var(--plum); stroke: var(--white); stroke-width: 4; }
  .diamond { fill: var(--white); }

  .quote-hand { font-family: "Short Stack", "Sniglet", cursive; fill: var(--sky); }
  .quote-big { font-family: "Sniglet", "Short Stack", cursive; fill: var(--sky); }
  .quote-key { font-family: "Short Stack", cursive; fill: var(--red); }
  .quote-credit { font-family: "Tinos", serif; fill: var(--sky); }

  .script-title { font-family: "Pinyon Script", cursive; fill: var(--plum-text); }

  .beach-outline { font-family: "Short Stack", cursive; fill: var(--white); stroke: var(--coral); stroke-width: 3; }
  .beach-bold { font-family: "Titan One", sans-serif; fill: var(--coral); }
  .beach-caps { font-family: "Lilita One", sans-serif; fill: var(--coral); }
  .beach-hand { font-family: "Gochi Hand", cursive; fill: var(--coral); }

  .art-flowers-warm { fill: var(--petal-orange); }
  .art-flowers-pink { fill: var(--petal-pink); }
  .art-noodles { fill: none; stroke: var(--noodle); stroke-width: 4; }
  .art-glass { fill: var(--red); stroke: var(--white); stroke-width: 4; }
  .art-bottle { fill: var(--red); stroke: var(--white); stroke-width: 4; }
</style>
</head>
<body>
<svg class="towel-set" viewBox="0 0 1460 845" xmlns="http://www.w3.org/2000/svg">

  <!-- Towel one: spaghetti quote -->
  <g class="towel towel-spaghetti">
    <rect class="fill-sky" x="42" y="38" width="141" height="767"/>
    <rect class="fill-sky-light" x="100" y="38" width="25" height="767"/>
    <rect class="fill-teal" x="190" y="38" width="143" height="767"/>
    <rect class="fill-sky" x="340" y="38" width="142" height="767"/>
    <rect class="fill-sky-light" x="398" y="38" width="25" height="767"/>

    <path class="badge" d="M260,172 C300,205 360,225 420,228 C410,265 440,290 452,320 L452,598 C400,615 300,640 260,690 C220,640 120,615 72,598 L72,320 C80,290 110,265 100,228 C160,225 220,205 260,172 Z"/>

    <ellipse class="art-flowers-warm" role="img" aria-label="Orange and red flowers" cx="190" cy="205" rx="65" ry="40"/>
    <ellipse class="art-flowers-pink" role="img" aria-label="Pink and purple flowers" cx="375" cy="165" rx="75" ry="45"/>

    <text class="quote-hand" x="262" y="312" font-size="54" text-anchor="middle">Everything</text>
    <text class="quote-big" x="258" y="408" font-size="100" text-anchor="middle">I am,</text>
    <text class="quote-hand" x="262" y="470" font-size="54" text-anchor="middle">i owe to</text>
    <text class="quote-key" x="265" y="540" font-size="88" text-anchor="middle" textLength="410" lengthAdjust="spacingAndGlyphs">Spaghetti</text>
    <text class="quote-credit" x="446" y="575" font-size="27" text-anchor="end">- Marta Velucci</text>

    <ellipse class="art-noodles" role="img" aria-label="Swirl of spaghetti" cx="405" cy="608" rx="58" ry="18"/>
  </g>

  <!-- Towel two: desperate housewife -->
  <g class="towel towel-housewife">
    <rect class="fill-wine" x="510" y="38" width="440" height="767"/>
    <rect class="fill-white" x="603" y="38" width="83" height="767"/>
    <rect class="fill-red" x="605" y="38" width="12" height="767"/>
    <rect class="fill-red" x="672" y="38" width="12" height="767"/>
    <rect class="fill-white" x="777" y="38" width="80" height="767"/>
    <rect class="fill-red" x="779" y="38" width="10" height="767"/>
    <rect class="fill-red" x="845" y="38" width="12" height="767"/>

    <path class="banner" d="M510,265 C600,270 690,250 730,205 C770,250 860,270 950,265 L950,545 C860,540 770,560 730,625 C690,560 600,540 510,545 Z"/>

    <rect class="art-glass" role="img" aria-label="Glass of red wine" x="842" y="240" width="80" height="150" rx="30"/>
    <rect class="art-bottle" role="img" aria-label="Tilted wine bottle" x="530" y="405" width="80" height="155" rx="20" transform="rotate(12 570 480)"/>

    <text class="script-title" x="690" y="385" font-size="78" text-anchor="middle">Desperate</text>
    <text class="script-title" x="780" y="465" font-size="78" text-anchor="middle">Housewife</text>
  </g>

  <!-- Towel three: Sydney beaches -->
  <g class="towel towel-beaches">
    <rect class="fill-sky" x="978" y="38" width="215" height="767"/>
    <rect class="fill-sky-deep" x="1062" y="38" width="52" height="767"/>
    <rect class="fill-sun" x="1200" y="38" width="218" height="767"/>
    <rect class="fill-tangerine" x="1282" y="38" width="57" height="767"/>

    <path class="diamond" d="M1200,168 L1412,385 L1200,672 L985,385 Z"/>

    <text class="beach-outline" x="1197" y="238" font-size="72" text-anchor="middle">Coogee</text>
    <text class="beach-bold" x="1200" y="332" font-size="76" text-anchor="middle">Bronte</text>
    <text class="beach-caps" x="1197" y="432" font-size="96" text-anchor="middle" textLength="400" lengthAdjust="spacingAndGlyphs">CLOVELLY</text>
    <text class="beach-hand" x="1197" y="528" font-size="92" text-anchor="middle" textLength="355" lengthAdjust="spacingAndGlyphs">Tamarama</text>
    <text class="beach-outline" x="1198" y="633" font-size="80" text-anchor="middle">Bondi</text>
  </g>
</svg>
</body>
</html>
```